Real Estate Investing company needs a business card design

We need a business card design for new Real Estate Investment Company called "Maple Ridge Ventures, LLC." We buy homes for cash and close quickly in any situation. Our company provides an easy and fast option for home owners who are in tough situations who need to sell their home fast and don't want realtor fees or other listing hassles. We also renovate and resell our homes which helps provide housing for the community. We would like to see designs that use the colors blue and white to match our company logo or other colors that may match our company logo. The final design should communicate trust and easy process.
Industry/Entity Type
Business
Contact Information for Business Card
Front should have company name and company logo. back of card should have company logo and area to list services.
Look and feel

```html
<!DOCTYPE html>
<html lang="en">
<head>
<meta charset="utf-8">
<title>Maple Ridge Ventures – Business Cards</title>
<link rel="stylesheet" href="https://fonts.googleapis.com/css2?family=Open+Sans:wght@400;600;700&display=swap">
<style>
  :root {
    --brand-blue: #1e6fc2;
    --card-white: #f7f7f7;
    --arc-grey: #cfcfcf;
    --stage: #e6e6e6;
    --text-white: #ffffff;
  }
  * { box-sizing: border-box; margin: 0; padding: 0; }
  html, body {
    width: 1200px; height: 716px; overflow: hidden;
    background: var(--stage);
    font-family: "Open Sans", Arial, sans-serif;
  }
  .stage {
    position: relative; width: 1200px; height: 716px;
    display: flex; align-items: center; justify-content: center; gap: 40px;
  }
  .card {
    position: relative; width: 540px; height: 310px;
    background: var(--card-white); overflow: hidden;
    box-shadow: 0 2px 8px rgba(0,0,0,.15);
  }

  /* Services side */
  .services-card .brand-name {
    position: absolute; left: 0; right: 0; top: 40px;
    display: flex; align-items: center; justify-content: center; gap: 12px;
    color: var(--brand-blue); font-weight: 700; font-size: 30px; line-height: 1;
    letter-spacing: .5px;
  }
  .brand-mark { width: 16px; height: 16px; background: var(--brand-blue); flex: none; }
  .services-card .band {
    position: absolute; left: 0; right: 0; top: 118px; height: 92px;
    background: var(--brand-blue); color: var(--text-white);
    display: flex; align-items: center; justify-content: center;
    text-align: center; font-size: 15px; line-height: 1.45; padding: 0 40px;
  }
  .band strong { font-weight: 700; }
  .services-card .website-note {
    position: absolute; left: 0; right: 0; top: 228px;
    text-align: center; color: var(--brand-blue); font-size: 14px;
  }

  /* Contact side */
  .contact-card .curve { position: absolute; inset: 0; }
  .contact-card .brand-name {
    position: absolute; left: 24px; top: 122px;
    display: flex; align-items: center; gap: 8px;
    color: var(--brand-blue); font-weight: 700; font-size: 18px; line-height: 1.2;
  }
  .contact-card .details {
    position: absolute; left: 282px; top: 88px; color: var(--text-white);
  }
  .person-name { font-size: 22px; font-weight: 700; letter-spacing: .5px; }
  .person-title { font-size: 12px; margin-bottom: 16px; }
  .contact-line { display: flex; align-items: center; gap: 9px; font-size: 12px; line-height: 1.7; }
  .contact-line svg { width: 12px; height: 12px; flex: none; }
  .address { font-size: 12px; line-height: 1.5; margin-top: 2px; max-width: 220px; }
</style>
</head>
<body>
<main class="stage">
  <section class="card services-card">
    <div class="brand-name"><span class="brand-mark"></span>MAPLE RIDGE VENTURES</div>
    <div class="band">
      <p><strong>Services:</strong> Dryer Vent Cleaning, A/C Duct Cleaning, Air Conditioning, Camera Inspections.</p>
    </div>
    <p class="website-note">Please visit our website to find out more: www.mapleridgeventures.com</p>
  </section>

  <section class="card contact-card">
    <svg class="curve" viewBox="0 0 540 310" preserveAspectRatio="none" aria-hidden="true">
      <path d="M320 0 Q190 130 168 310" fill="none" stroke="var(--arc-grey)" stroke-width="14"/>
      <path d="M338 0 Q208 130 188 310 H540 V0 Z" fill="var(--brand-blue)"/>
    </svg>
    <div class="brand-name"><span class="brand-mark"></span><span>MAPLE RIDGE<br>VENTURES</span></div>
    <div class="details">
      <p class="person-name">YOUR NAME</p>
      <p class="person-title">Managing Director</p>
      <p class="contact-line">
        <svg viewBox="0 0 12 12"><path d="M2 1h3l1 3-2 1a7 7 0 0 0 3 3l1-2 3 1v3c-6 0-9-3-9-9z" fill="#fff"/></svg>
        +00 111 222 3333</p>
      <p class="contact-line">
        <svg viewBox="0 0 12 12"><rect x="1" y="2.5" width="10" height="7" fill="#fff"/><path d="M1 2.5l5 4 5-4" fill="none" stroke="#1e6fc2"/></svg>
        yourname@mapleridgeventures.com</p>
      <p class="contact-line">
        <svg viewBox="0 0 12 12"><circle cx="6" cy="6" r="5" fill="none" stroke="#fff"/><path d="M1 6h10M6 1c-3 3-3 7 0 10M6 1c3 3 3 7 0 10" fill="none" stroke="#fff" stroke-width=".8"/></svg>
        www.mapleridgeventures.com</p>
      <p class="address">Your Long Commercial or business address in 2 line with pincode</p>
    </div>
  </section>
</main>
</body>
</html>
```